Business Card Design for venture capital-focused company

I have a logo (attached), and would like business cards designed using the attached logo. Audience is mainly financial executives; services included finance/ accounting/ dashboards/ etc. Open to different design ideas. Thanks for your consideration.

Target Market(s)

Financial Executives, Venture Capital, etc.

Industry/Entity Type

Venture Capital

Contact Information for Business Card

Harbor Ledger Insights LLC
418 N Wexley Street
Cedar Brook, OH 60214

Font styles to use
Serif
Sans Serif

```html
<!DOCTYPE html>
<html lang="en">
<head>
<meta charset="utf-8">
<title>Harbor Ledger Insights – Business Cards</title>
<link rel="stylesheet" href="https://fonts.googleapis.com/css2?family=Montserrat:wght@600;700&family=Roboto:wght@400;500&display=swap">
<style>
  :root {
    --brand-blue: #2353a5;
    --ink: #3a3a3a;
    --rule-grey: #9a9a9a;
    --band-grey: #6b6b6b;
    --card-white: #ffffff;
    --page-bg: #e9eaec;
  }
  * { box-sizing: border-box; margin: 0; padding: 0; }
  html, body {
    width: 1200px; height: 864px; overflow: hidden;
    background: var(--page-bg);
    font-family: "Roboto", Arial, sans-serif;
  }
  .sheet {
    position: relative; width: 1200px; height: 864px;
    display: flex; align-items: center; justify-content: center; gap: 20px;
  }
  .card {
    position: relative; width: 560px; height: 320px; overflow: hidden;
    box-shadow: 0 2px 10px rgba(0,0,0,0.12);
  }

  /* Front */
  .card--front {
    background: var(--brand-blue);
    display: flex; align-items: center; justify-content: center;
  }
  .wordmark {
    display: flex; align-items: center; gap: 12px;
    font-family: "Roboto", Arial, sans-serif; font-weight: 500;
    letter-spacing: 0.08em; text-transform: uppercase; line-height: 1.1;
    white-space: nowrap;
  }
  .wordmark__dot { width: 14px; height: 14px; border-radius: 50%; flex: none; }
  .card--front .wordmark { color: var(--card-white); font-size: 34px; }
  .card--front .wordmark__dot { background: var(--card-white); }

  /* Back */
  .card--back { background: var(--card-white); }
  .card--back .wordmark {
    position: absolute; left: 34px; top: 112px;
    color: var(--brand-blue); font-size: 20px; gap: 10px;
  }
  .card--back .wordmark__dot { width: 12px; height: 12px; background: var(--brand-blue); }
  .divider {
    position: absolute; left: 268px; top: 78px; width: 1px; height: 112px;
    background: var(--rule-grey);
  }
  .contact { position: absolute; left: 292px; top: 74px; }
  .contact__name {
    font-family: "Montserrat", Arial, sans-serif; font-weight: 700;
    font-size: 19px; color: var(--brand-blue); letter-spacing: 0.01em;
  }
  .contact__title {
    font-family: "Montserrat", Arial, sans-serif; font-weight: 600;
    font-size: 14px; color: var(--ink); margin-top: 2px;
  }
  .contact__list { list-style: none; margin-top: 14px; }
  .contact__item {
    display: flex; align-items: center; gap: 8px;
    font-size: 15px; color: var(--ink); line-height: 21px;
  }
  .contact__icon { width: 12px; height: 12px; flex: none; }
  .company {
    position: absolute; left: 0; right: 0; top: 216px; text-align: center;
  }
  .company__name { font-size: 17px; color: var(--brand-blue); }
  .company__address { font-size: 16px; color: var(--ink); margin-top: 2px; }
  .base-band { position: absolute; left: 0; bottom: 0; width: 560px; height: 22px; }
</style>
</head>
<body>
<main class="sheet">
  <section class="card card--front" aria-label="Card front">
    <div class="wordmark">
      <span class="wordmark__dot"></span>
      <span class="wordmark__text">Harbor Ledger<br>Insights</span>
    </div>
  </section>

  <section class="card card--back" aria-label="Card back">
    <div class="wordmark">
      <span class="wordmark__dot"></span>
      <span class="wordmark__text">Harbor Ledger<br>Insights</span>
    </div>
    <div class="divider"></div>
    <div class="contact">
      <p class="contact__name">MARCUS WHITFIELD</p>
      <p class="contact__title">Principal</p>
      <ul class="contact__list">
        <li class="contact__item">
          <svg class="contact__icon" viewBox="0 0 12 12"><path fill="var(--brand-blue)" d="M2.5 1l2 2-1 1.3a7 7 0 0 0 4.2 4.2L9 7.5l2 2-1.3 1.5C5.5 11 1 6.5 1 2.3z"/></svg>
          555-214-7730
        </li>
        <li class="contact__item">
          <svg class="contact__icon" viewBox="0 0 12 12"><rect x="0.5" y="2.5" width="11" height="7.5" rx="1" fill="var(--brand-blue)"/><path d="M1 3l5 4 5-4" stroke="#fff" stroke-width="1" fill="none"/></svg>
          mw@harborledger.com
        </li>
        <li class="contact__item">
          <svg class="contact__icon" viewBox="0 0 12 12" fill="none" stroke="var(--brand-blue)" stroke-width="1.1"><circle cx="6" cy="6" r="5"/><ellipse cx="6" cy="6" rx="2.2" ry="5"/><path d="M1 6h10"/></svg>
          www.harborledger.com
        </li>
      </ul>
    </div>
    <div class="company">
      <p class="company__name">Harbor Ledger Insights LLC</p>
      <p class="company__address">418 N Wexley Street Cedar Brook, OH 60214</p>
    </div>
    <svg class="base-band" viewBox="0 0 560 22" preserveAspectRatio="none" aria-hidden="true">
      <polygon points="0,10 390,10 384,22 0,22" fill="var(--brand-blue)"/>
      <polygon points="394,10 560,2 560,22 388,22" fill="var(--band-grey)"/>
    </svg>
  </section>
</main>
</body>
</html>
```